Property Management Company Business Cards

Need business cards for a property management company located in Michigan. We manage houses for clients all over the world. Young and modern company, looking for eye catching design. Please work with the attached logo.

Industry/Entity Type

Property Management

Requirements
Must have
• Need lines for address, telephone number, fax number, web site.

Also lines for name, and job title

```html
<!DOCTYPE html>
<html lang="en">
<head>
<meta charset="utf-8">
<title>Lakeshore Harbor Management – Business Cards</title>
<link rel="stylesheet" href="https://fonts.googleapis.com/css2?family=Open+Sans:wght@400;600;700&display=swap">
<style>
  :root {
    --stage: #2e2e30;
    --card-dark: #3b3b3d;
    --card-light: #ffffff;
    --accent: #1aa7e8;
    --ink: #3a3a3a;
    --rule: #4a4a4c;
    --brand-text: #ffffff;
  }
  * { margin: 0; padding: 0; box-sizing: border-box; }
  html, body {
    width: 1200px; height: 900px; overflow: hidden;
    background: var(--stage);
    font-family: "Open Sans", Arial, sans-serif;
  }
  .card {
    position: absolute;
    width: 515px; height: 285px;
    top: 307px;
    overflow: hidden;
    box-shadow: 0 4px 12px rgba(0,0,0,0.45);
  }
  .card--front { left: 73px; background: var(--card-dark); }
  .card--back { left: 615px; background: var(--card-light); }

  .brand {
    position: absolute;
    display: flex; align-items: center; gap: 9px;
    color: var(--brand-text);
    font-weight: 700;
    white-space: nowrap;
  }
  .brand__dot {
    width: 30px; height: 30px; border-radius: 50%;
    background: var(--accent); flex: none;
  }
  .brand__name { font-size: 16px; letter-spacing: 0.1px; line-height: 1; }
  .card--front .brand { left: 114px; top: 126px; }

  .back__swoosh { position: absolute; left: 0; top: 0; width: 515px; height: 285px; }
  .card--back .brand { left: 118px; top: 215px; }

  .person { position: absolute; left: 43px; top: 83px; }
  .person__name { color: var(--accent); font-size: 17px; font-weight: 700; line-height: 1.2; }
  .person__title { color: var(--ink); font-size: 12px; font-weight: 700; margin-top: 2px; }

  .divider {
    position: absolute; left: 266px; top: 41px;
    width: 1px; height: 124px; background: var(--rule);
  }

  .contact {
    position: absolute; right: 42px; top: 51px;
    list-style: none; text-align: right;
    color: var(--ink); font-size: 12px; line-height: 15.5px;
  }
  .contact li { display: flex; justify-content: flex-end; align-items: center; gap: 6px; }
  .contact li.gap { margin-top: 8px; }
  .contact .icon { width: 10px; height: 11px; flex: none; }
  .contact .icon--blank { visibility: hidden; }
</style>
</head>
<body>

<section class="card card--front" aria-label="Card front">
  <div class="brand">
    <span class="brand__dot"></span>
    <span class="brand__name">LAKESHORE HARBOR MANAGEMENT</span>
  </div>
</section>

<section class="card card--back" aria-label="Card back">
  <svg class="back__swoosh" viewBox="0 0 515 285" aria-hidden="true">
    <path d="M0 192 C140 196 360 190 515 158 L515 285 L0 285 Z" fill="var(--card-dark)"/>
    <path d="M70 189 C250 188 410 176 515 150 L515 156 C410 182 260 192 70 189 Z" fill="var(--card-dark)"/>
  </svg>

  <div class="person">
    <p class="person__name">Daniel Brooks</p>
    <p class="person__title">managing director</p>
  </div>

  <div class="divider"></div>

  <ul class="contact">
    <li>48 Harbor Lane
      <svg class="icon" viewBox="0 0 10 12"><path d="M5 0a4 4 0 0 0-4 4c0 3 4 8 4 8s4-5 4-8a4 4 0 0 0-4-4zm0 5.6A1.6 1.6 0 1 1 5 2.4a1.6 1.6 0 0 1 0 3.2z" fill="var(--accent)"/></svg></li>
    <li>Lakeview, Michigan 49001<span class="icon icon--blank"></span></li>
    <li>616 555 01 20
      <svg class="icon" viewBox="0 0 10 12"><rect x="2" y="0.5" width="6" height="11" rx="1" fill="none" stroke="var(--accent)" stroke-width="1.2"/><rect x="4" y="9" width="2" height="1" fill="var(--accent)"/></svg></li>
    <li>616 555 01 21
      <svg class="icon" viewBox="0 0 10 12"><rect x="2.5" y="1" width="5" height="3" fill="var(--accent)"/><rect x="0.5" y="4.5" width="9" height="5" rx="1" fill="var(--accent)"/><rect x="2.5" y="8" width="5" height="3" fill="var(--accent)"/></svg></li>
    <li class="gap">info@example.com
      <svg class="icon" viewBox="0 0 10 12"><rect x="0.5" y="3" width="9" height="6.5" fill="var(--accent)"/><path d="M0.5 3 L5 6.8 L9.5 3" fill="none" stroke="#fff" stroke-width="0.9"/></svg></li>
    <li>www.example.com
      <svg class="icon" viewBox="0 0 10 12"><circle cx="5" cy="6" r="4.3" fill="none" stroke="var(--accent)" stroke-width="1.1"/><ellipse cx="5" cy="6" rx="1.8" ry="4.3" fill="none" stroke="var(--accent)" stroke-width="0.9"/><path d="M0.7 6h8.6" stroke="var(--accent)" stroke-width="0.9"/></svg></li>
  </ul>

  <div class="brand">
    <span class="brand__dot"></span>
    <span class="brand__name">LAKESHORE HARBOR MANAGEMENT</span>
  </div>
</section>

</body>
</html>
```